KLV Messaging - veteran and exclusive boutique copywriting agency

PROJECT NEEDS:
1. Website design - full homepage design and inner page top banner design
2. Logo design
* Please see attached Briefs (Word Docs) for descriptions of what is needed for 1 and 2 above.
ABOUT THE CLIENT:
KLV Messaging is a veteran and exclusive boutique copywriting agency run by Marcus Holloway. Marcus is an award-winning published novelist and an accomplished executive ghostwriter with articles regularly published prominent technology publications like Brisk, ByteHarbor, FoundryPulse, and more. For nearly three decades, Marcus has focused solely on the technology sector - serving clients in Israel, Europe and the US.

Target Market(s)

hi-tech companies run by serious, confident professionals.

Industry/Entity Type

Business

Number of Pages Required

2 page

Font styles to use
Sans Serif
Other font styles liked:
• font should be modern

Colors
0054AA
0677BA
7BADD7
CADEEF
E8F1F8
F0912C
F2A743
F7CA91
FBE8D2
FDF5EE

Requirements
Must have
• psd files for logo, homepage design, and inner page top banner design
Nice to have
• Please see attached Website and Logo Design Briefs (Word Docs)
Should not have

```html
<!DOCTYPE html>
<html lang="en">
<head>
<meta charset="utf-8">
<title>KLV Messaging — Your Voice, My Words</title>
<link rel="stylesheet" href="https://fonts.googleapis.com/css2?family=Montserrat:ital,wght@0,400;0,500;0,600;0,700;1,400&family=Oswald:wght@300;600&display=swap">
<style>
  :root{
    --navy:#2a4574;
    --navy-dark:#223a63;
    --orange:#f7a823;
    --orange-deep:#ef9a12;
    --orange-pale:#fde7bf;
    --ink:#1d1d1f;
    --body:#2e2e33;
    --white:#ffffff;
  }
  *{box-sizing:border-box;margin:0;padding:0}
  html,body{width:1200px;height:3822px;overflow:hidden}
  body{position:relative;background:var(--white);font-family:"Montserrat",sans-serif;color:var(--body)}
  .abs{position:absolute}
  .backdrop{position:absolute;left:0;top:0;width:1200px;height:3822px}

  .brand{position:absolute;font-family:"Montserrat",sans-serif;font-weight:700;white-space:nowrap}
  .brand-header{left:162px;top:30px;font-size:30px;line-height:36px;color:var(--navy)}
  .brand-footer{left:786px;top:3594px;width:256px;text-align:center;font-size:34px;line-height:40px;color:var(--white)}

  .nav{position:absolute;top:38px;left:0;width:1200px;font-size:13.5px;color:var(--ink)}
  .nav a{position:absolute;color:inherit;text-decoration:none}
  .btn{position:absolute;display:flex;align-items:center;justify-content:center;border-radius:16px;font-size:14px;text-decoration:none}
  .btn-orange{background:var(--orange);color:var(--white)}
  .btn-navy{background:var(--navy);color:var(--white)}

  .hero-title{position:absolute;left:162px;top:150px;font-family:"Oswald",sans-serif;text-transform:uppercase}
  .hero-title .l1{display:block;font-weight:300;font-size:62px;line-height:68px;color:var(--ink)}
  .hero-title .l2{display:block;font-weight:600;font-size:76px;line-height:80px;color:var(--orange)}
  .hero-copy{position:absolute;left:162px;top:308px;width:310px;font-size:15px;line-height:24px;color:var(--ink)}
  .photo{position:absolute}

  .clients{position:absolute;top:636px;left:0;width:1200px;height:40px}
  .client{position:absolute;top:0;transform:translateX(-50%);display:flex;align-items:center;gap:8px;font-weight:700;font-size:22px;color:var(--white);white-space:nowrap;line-height:40px}
  .client .dot{width:14px;height:14px;border-radius:50%;background:var(--white)}
  .arrow-btn{position:absolute;width:26px;height:26px;border-radius:50%;border:1.5px solid currentColor;display:flex;align-items:center;justify-content:center}

  .h2{font-weight:500;font-size:38px;line-height:44px;color:var(--ink)}
  .eyebrow{font-weight:500;font-size:22px;color:var(--orange)}
  .para{font-size:13.5px;line-height:24px;color:var(--body)}

  .frame{position:absolute;background:var(--white);box-shadow:0 6px 22px rgba(0,0,0,.12)}

  .card{position:absolute;top:1441px;width:270px;height:252px;background:var(--navy);border-radius:8px 8px 4px 4px;color:var(--white);text-align:center}
  .card-reflection{position:absolute;top:1697px;width:270px;height:70px;background:linear-gradient(#e3e6eb,rgba(236,238,242,0));border-radius:4px}
  .card-icon{position:absolute;left:50%;top:-70px;width:136px;height:136px;margin-left:-68px;border-radius:50%;background:linear-gradient(160deg,var(--orange),var(--orange-deep));border:5px solid var(--white);display:flex;align-items:center;justify-content:center;box-shadow:0 4px 12px rgba(0,0,0,.18)}
  .card-title{position:absolute;top:82px;width:100%;font-weight:600;font-size:19px;color:var(--orange)}
  .card-sub{position:absolute;top:112px;width:100%;font-weight:600;font-size:13px;color:var(--white)}
  .card-body{position:absolute;top:138px;left:10px;right:10px;font-size:13px;line-height:24px}

  .centered{position:absolute;left:0;width:1200px;text-align:center}

  .reason{position:absolute;left:170px;width:370px}
  .reason-icon{position:absolute;left:10px;top:6px;width:60px;height:60px;border-radius:50%;background:var(--orange-pale)}
  .reason-text{position:absolute;left:92px;top:0;width:280px;font-size:13px;line-height:24px;color:var(--ink)}
  .reason-text b{font-weight:600}

  .quote-card{position:absolute;left:282px;top:2632px;width:648px;height:163px;background:var(--white);box-shadow:0 6px 18px rgba(0,0,0,.08);border-bottom:4px solid var(--orange);text-align:center}
  .quote-card q{display:block;margin:42px auto 0;width:580px;font-style:italic;font-size:13px;line-height:24px;color:var(--ink);quotes:none}
  .quote-card cite{display:block;margin-top:10px;font-style:normal;font-weight:600;font-size:12px;color:var(--ink)}

  .about-lede{font-style:italic;font-size:13px;line-height:24px;color:var(--orange)}

  .footer{position:absolute;left:0;top:3451px;width:1200px;height:325px;background:var(--navy)}
  .footer-bar{position:absolute;left:0;top:3776px;width:1200px;height:46px;background:var(--navy-dark);color:var(--white);font-size:11px;display:flex;align-items:center;justify-content:center}
  .f-head{position:absolute;font-weight:600;font-size:13px;color:var(--white)}
  .f-rule{position:absolute;height:3px;width:34px;background:var(--orange)}
  .f-link{position:absolute;font-size:12px;color:var(--white);text-decoration:none}
  .f-divider{position:absolute;top:3560px;width:1px;height:192px;background:rgba(255,255,255,.2)}
  .f-contact{position:absolute;left:547px;font-size:12px;line-height:22px;color:var(--white)}
  .social{position:absolute;top:3690px;width:24px;height:24px;border-radius:50%;background:var(--white);border:2px solid #4a90d9}
</style>
</head>
<body>

<svg class="backdrop" viewBox="0 0 1200 3822" aria-hidden="true">
  <defs>
    <linearGradient id="heroShade" x1="0" y1="0" x2="1" y2="1">
      <stop offset="0" stop-color="#ffffff"/>
      <stop offset="1" stop-color="#ecedf0"/>
    </linearGradient>
    <linearGradient id="greyBand" x1="0" y1="0" x2="0" y2="1">
      <stop offset="0" stop-color="#f1f2f5"/>
      <stop offset="1" stop-color="#e7e9ed"/>
    </linearGradient>
  </defs>
  <rect x="0" y="0" width="1200" height="727" fill="url(#heroShade)"/>
  <circle cx="0" cy="66" r="154" fill="none" stroke="#e4e6eb" stroke-width="12"/>
  <polygon points="0,522 823,606 1200,497 1200,515 823,620 0,542" fill="var(--navy)"/>
  <polygon points="0,542 823,620 1200,515 1200,727 0,727" fill="var(--orange)"/>
  <polygon points="0,1300 1200,1214 1200,1770 0,1770" fill="url(#greyBand)"/>
  <polygon points="0,2568 1200,2504 1200,2870 0,2870" fill="url(#greyBand)"/>
  <polygon points="601,2062 700,1975 1023,1972 1023,2521 601,2480" fill="var(--orange)"/>
  <g fill="#d6d9df">
    <g transform="translate(1160,232)">
      <circle cx="0" cy="0" r="2"/><circle cx="12" cy="0" r="2"/><circle cx="24" cy="0" r="2"/><circle cx="36" cy="0" r="2"/>
      <circle cx="0" cy="14" r="2"/><circle cx="12" cy="14" r="2"/><circle cx="24" cy="14" r="2"/><circle cx="36" cy="14" r="2"/>
      <circle cx="0" cy="28" r="2"/><circle cx="12" cy="28" r="2"/><circle cx="24" cy="28" r="2"/><circle cx="36" cy="28" r="2"/>
      <circle cx="0" cy="42" r="2"/><circle cx="12" cy="42" r="2"/><circle cx="24" cy="42" r="2"/><circle cx="36" cy="42" r="2"/>
      <circle cx="0" cy="56" r="2"/><circle cx="12" cy="56" r="2"/><circle cx="24" cy="56" r="2"/><circle cx="36" cy="56" r="2"/>
    </g>
    <g transform="translate(128,783)">
      <circle cx="0" cy="0" r="2"/><circle cx="16" cy="0" r="2"/><circle cx="32" cy="0" r="2"/><circle cx="48" cy="0" r="2"/><circle cx="64" cy="0" r="2"/>
      <circle cx="0" cy="16" r="2"/><circle cx="16" cy="16" r="2"/><circle cx="32" cy="16" r="2"/><circle cx="48" cy="16" r="2"/><circle cx="64" cy="16" r="2"/>
      <circle cx="0" cy="32" r="2"/><circle cx="16" cy="32" r="2"/><circle cx="32" cy="32" r="2"/><circle cx="48" cy="32" r="2"/><circle cx="64" cy="32" r="2"/>
      <circle cx="0" cy="48" r="2"/><circle cx="16" cy="48" r="2"/><circle cx="32" cy="48" r="2"/><circle cx="48" cy="48" r="2"/><circle cx="64" cy="48" r="2"/>
      <circle cx="0" cy="64" r="2"/><circle cx="16" cy="64" r="2"/><circle cx="32" cy="64" r="2"/><circle cx="48" cy="64" r="2"/><circle cx="64" cy="64" r="2"/>
    </g>
    <g transform="translate(988,1950)">
      <circle cx="0" cy="0" r="2"/><circle cx="16" cy="0" r="2"/><circle cx="32" cy="0" r="2"/><circle cx="48" cy="0" r="2"/><circle cx="64" cy="0" r="2"/>
      <circle cx="0" cy="16" r="2"/><circle cx="16" cy="16" r="2"/><circle cx="32" cy="16" r="2"/><circle cx="48" cy="16" r="2"/><circle cx="64" cy="16" r="2"/>
      <circle cx="48" cy="32" r="2"/><circle cx="64" cy="32" r="2"/>
      <circle cx="48" cy="48" r="2"/><circle cx="64" cy="48" r="2"/>
    </g>
  </g>
</svg>

<!-- header -->
<div class="brand brand-header">KLV Messaging</div>
<nav class="nav">
  <a style="left:578px">Home</a>
  <a style="left:638px">About</a>
  <a style="left:704px">Industries</a>
  <a style="left:788px">Portfolio</a>
  <a style="left:871px">Clients</a>
</nav>
<a class="btn btn-orange" style="left:939px;top:32px;width:99px;height:30px">Contact</a>

<!-- hero -->
<h1 class="hero-title"><span class="l1">Your voice,</span><span class="l2">My words.</span></h1>
<p class="hero-copy">Copywriting and executive ghostwriting that speaks for your vision and your technology.</p>
<a class="btn btn-navy" style="left:162px;top:396px;width:99px;height:30px">Contact</a>
<div class="photo" role="img" aria-label="Portrait of Marcus Holloway standing, light blue shirt and jeans" style="left:684px;top:66px;width:212px;height:526px;border-radius:90px 90px 10px 10px;background:linear-gradient(180deg,#d9d4cf 0%,#a9bfdc 30%,#8eaad2 65%,#4a6284 100%)"></div>

<!-- client strip -->
<div class="clients">
  <span class="arrow-btn" style="left:100px;top:7px;color:#fff"><svg width="10" height="10" viewBox="0 0 10 10"><path d="M6.5 1.5 3 5l3.5 3.5" fill="none" stroke="#fff" stroke-width="1.5"/></svg></span>
  <span class="client" style="left:222px"><span class="dot"></span>Northvane</span>
  <span class="client" style="left:400px">Kestrel</span>
  <span class="client" style="left:593px">Quillbay</span>
  <span class="client" style="left:783px"><span class="dot"></span>Tandrix</span>
  <span class="client" style="left:971px">Ferrowave</span>
  <span class="arrow-btn" style="left:1068px;top:7px;color:#fff"><svg width="10" height="10" viewBox="0 0 10 10"><path d="M3.5 1.5 7 5 3.5 8.5" fill="none" stroke="#fff" stroke-width="1.5"/></svg></span>
</div>

<!-- what I do -->
<div class="frame" style="left:162px;top:817px;width:409px;height:481px">
  <div role="img" aria-label="Portrait of Marcus Holloway in a light blue shirt against a dark backdrop" style="position:absolute;left:14px;top:15px;width:380px;height:451px;background:linear-gradient(135deg,#4b4e55 0%,#2c2e33 60%,#1e1f23 100%)"></div>
</div>
<h2 class="h2 abs" style="left:624px;top:845px">What I do</h2>
<div class="eyebrow abs" style="left:624px;top:895px">Clear Words for Complex Technology</div>
<p class="para abs" style="left:624px;top:938px;width:420px">Lorem ipsum dolor sit amet, consectetuer adipiscing elit, sed diam nonummy nibh euismod tincidunt ut laoreet dolore magna aliquam erat volutpat. Ut wisi enim ad minim veniam, corper suscipit lobortis nisl ut aliquip ex ea commodo consequat.</p>
<p class="para abs" style="left:624px;top:1085px;width:420px">Duis autem vel eum iriure dolor in hendrerit in vulputate velit esse molestie consequat, vel illum dolore eu feugiat nulla facilisis .</p>

<!-- services -->
<div class="card" style="left:162px">
  <div class="card-icon">
    <svg width="70" height="70" viewBox="0 0 70 70" fill="none" stroke="#fff" stroke-width="2.5" stroke-linejoin="round"><rect x="6" y="10" width="40" height="28" rx="5"/><path d="M16 38v8l8-8"/><rect x="22" y="22" width="42" height="30" rx="5" fill="#f3a01d"/><path d="M52 52v9l-9-9"/></svg>
  </div>
  <div class="card-title">Messaging</div>
  <div class="card-sub">The Value of a Fresh Perspective</div>
  <p class="card-body">Could you be reaching farther? Clearly-defined, accurately-targeted messaging is crucial.</p>
</div>
<div class="card-reflection" style="left:162px"></div>

<div class="card" style="left:464px">
  <div class="card-icon">
    <svg width="70" height="70" viewBox="0 0 70 70" fill="none" stroke="#fff" stroke-width="2.5" stroke-linejoin="round"><path d="M14 6h28l10 10v32H14z"/><path d="M42 6v10h10"/><path d="M20 22h14M20 30h22M20 38h16"/><circle cx="50" cy="52" r="11" fill="#f3a01d"/><path d="M45 52l4 4 7-8"/></svg>
  </div>
  <div class="card-title">Collateral</div>
  <div class="card-sub">Concise, Effective, Creative</div>
  <p class="card-body">Marketing collateral that effectively communicates who you are and what you want to say.</p>
</div>
<div class="card-reflection" style="left:464px"></div>

<div class="card" style="left:768px">
  <div class="card-icon">
    <svg width="70" height="70" viewBox="0 0 70 70" fill="none" stroke="#fff" stroke-width="2.5" stroke-linejoin="round"><path d="M10 12h32v48H10z"/><path d="M16 22h16M16 30h20M16 38h14M16 46h18"/><path d="M34 34 62 18 50 50l-8-9z" fill="#f3a01d"/><path d="M42 41 62 18"/></svg>
  </div>
  <div class="card-title">Content Marketing</div>
  <div class="card-sub">Giving Voice to Your Vision</div>
  <p class="card-body">Articles, blog content, white papers, e-books. Your ideas and expertise, our words.</p>
</div>
<div class="card-reflection" style="left:768px"></div>

<!-- why choose me -->
<h2 class="h2 centered" style="top:1808px">Why Choose Me</h2>
<p class="para centered" style="top:1866px;font-size:13px">In nearly two decades in the international marketing trenches, I've learned to rapidly define and<br>internalize company messages - and to communicate them at eye-level.</p>

<div class="reason" style="top:1978px">
  <div class="reason-icon" role="img" aria-label="Icon of two people in conversation"></div>
  <p class="reason-text">I do all client writing myself, so my clients get <b>one-on-one service</b> and a <b>personal guarantee of quality.</b></p>
</div>
<div class="reason" style="top:2098px">
  <div class="reason-icon" role="img" aria-label="Icon of a shirt and tie"></div>
  <p class="reason-text">My writing is <b>concise, elegant, and professional</b> - while at the same time reflecting an understated creativity and sense of humor that brings company messages to a very intimate, personal level.</p>
</div>
<div class="reason" style="top:2266px">
  <div class="reason-icon" role="img" aria-label="Icon of a cloud network"></div>
  <p class="reason-text">I offer clients a <b>deep understanding of business, communication, and technology</b> - coupled with a hard-hitting and concise, yet elegant writing style.</p>
</div>
<a class="btn btn-navy" style="left:262px;top:2391px;width:98px;height:30px">Contact</a>

<div class="photo" role="img" aria-label="Portrait of Marcus Holloway standing in a light blue shirt" style="left:678px;top:1946px;width:270px;height:560px;border-radius:100px 100px 6px 6px;background:linear-gradient(180deg,#d6cfc8 0%,#a9bfdc 28%,#8eaad2 65%,#4a6284 100%)"></div>

<!-- testimonials -->
<h2 class="h2 centered" style="top:2565px">What They’re Saying</h2>
<span class="arrow-btn" style="left:239px;top:2708px;color:#333"><svg width="10" height="10" viewBox="0 0 10 10"><path d="M6.5 1.5 3 5l3.5 3.5" fill="none" stroke="#333" stroke-width="1.5"/></svg></span>
<div class="quote-card">
  <q>Marcus is a terrific resource for our company. A self-starter, who has generated a great deal of revenue for us and does high-quality work. Highly recommended.</q>
  <cite>Dana Keller, CEO, Lumera Systems</cite>
</div>
<span class="arrow-btn" style="left:948px;top:2708px;color:#333"><svg width="10" height="10" viewBox="0 0 10 10"><path d="M3.5 1.5 7 5 3.5 8.5" fill="none" stroke="#333" stroke-width="1.5"/></svg></span>

<div class="footer"></div>

<!-- about -->
<div class="frame" style="left:162px;top:2954px;width:409px;height:556px">
  <div role="img" aria-label="Close-up portrait of Marcus Holloway in a brown jacket" style="position:absolute;left:14px;top:15px;width:380px;height:526px;background:linear-gradient(160deg,#c9c6c1 0%,#a39586 45%,#6b4f36 100%)"></div>
</div>
<h2 class="h2 abs" style="left:601px;top:2955px;width:420px;line-height:41px">About Marcus Holloway</h2>
<p class="about-lede abs" style="left:601px;top:3039px;width:422px">In nearly two decades in the international marketing trenches, I've learned to rapidly define and internalize company messages - and to communicate them at eye-level.</p>
<p class="para abs" style="left:601px;top:3120px;width:422px;font-size:13px">Born and raised in the US, I've lived and worked in Israel since 1990, and speak fluent Hebrew. I do all client writing myself, so my clients get one-on-one service and a personal guarantee of quality.</p>
<p class="para abs" style="left:601px;top:3241px;width:422px;font-size:13px">My writing is concise, elegant, and professional - while at the same time reflecting an understated creativity and sense of humor that brings company messages to a very intimate, personal level. I offer clients a deep understanding of business, communication, and technology - coupled with a hard-hitting and concise, yet elegant writing style.</p>

<!-- footer content -->
<div class="f-head" style="left:162px;top:3572px">Quick Links</div>
<div class="f-rule" style="left:162px;top:3598px"></div>
<a class="f-link" style="left:162px;top:3620px;text-decoration:underline">Home</a>
<a class="f-link" style="left:162px;top:3650px">About</a>
<a class="f-link" style="left:162px;top:3680px">Services</a>
<a class="f-link" style="left:162px;top:3710px">Industries</a>
<a class="f-link" style="left:263px;top:3622px">Portfolio</a>
<a class="f-link" style="left:263px;top:3652px">Clients</a>
<a class="f-link" style="left:263px;top:3682px">Contact</a>

<div class="f-divider" style="left:452px"></div>
<div class="f-divider" style="left:749px"></div>

<div class="f-head" style="left:522px;top:3572px">Contact Us</div>
<div class="f-rule" style="left:522px;top:3598px"></div>
<svg class="abs" style="left:523px;top:3620px" width="14" height="16" viewBox="0 0 14 16" fill="none" stroke="var(--orange)" stroke-width="1.5"><path d="M7 15s5-5 5-9A5 5 0 0 0 2 6c0 4 5 9 5 9z"/><circle cx="7" cy="6" r="1.8"/></svg>
<p class="f-contact" style="top:3614px">P.O. Box 5120<br>Harlow Bay, 40815</p>
<svg class="abs" style="left:522px;top:3678px" width="16" height="12" viewBox="0 0 16 12" fill="none" stroke="var(--orange)" stroke-width="1.5"><rect x="1" y="1" width="14" height="10"/><path d="m1 1 7 5 7-5"/></svg>
<p class="f-contact" style="top:3673px">studio@klvmessaging.net</p>
<svg class="abs" style="left:525px;top:3712px" width="10" height="16" viewBox="0 0 10 16" fill="none" stroke="var(--orange)" stroke-width="1.5"><rect x="1" y="1" width="8" height="14" rx="1.5"/><path d="M4 12.5h2"/></svg>
<p class="f-contact" style="top:3708px;font-size:14px">+972-55-210-6618</p>

<div class="brand brand-footer">KLV Messaging</div>
<span class="social" style="left:865px"></span>
<span class="social" style="left:894px"></span>
<span class="social" style="left:923px"></span>

<div class="footer-bar">© 2023 KLV Messaging. All Right Reserved.</div>

</body>
</html>
```